Online Digital Solutions Agency needs a New Business Card

We are a Online/Digital solution agency. We provide WordPress Solutions, Online & Digital Marketing Solutions including SEO, Social Media Marketing and Managed Hosting including VPS and Cloud Hosting solutions. We also design and build bespoke web sites and web applications for various clients. We are very good at site migrations, 3rd party API integrations and mobile app development.

We are rebranding our agency and have already designed a new logo. We have selected 5-6 colours as our base colour and are currently building our new website based around these colour scheme.

Our logo indicates that we are a cloud solution providers, and (i.e. the Clouds), and developers (i.e. HTML Tags, and CSS formats). We use the 5-6 base colours and use various shades of these colours as required.

Our old website is located at: www.brambleforgelabs.com

And our new website is going to be at (we are working on it at the moment ...):
https://creative.brambleforgelabs.co.uk/

Our slogan is "Digital Transformation Specialist"

What we mean by that is; we can take any existing business and get them up and transform them in to the digital world, starting with Hosting, Web Design, Development & Online Marketing aspects.

The powerpoint is a document that we use to present our projects to clients at the moment, and the cloud is on the background as we clarified earlier. (Just to get the idea)

What we are looking for is a Great WoW factor design to start with, ideally with the Logo and Logo colour scheme if possible but not required as long as the designers can do better, and basically give life to our logo and company via the Business card design.

Ideally with some icons perhaps to indicate the address, location, mobile, email, and website would be good but again optional as long as there is a good design.

The cloud can be used as a background if required in a light shade or as a watermark share perhaps.

The logos' and the Illustrator files are shared with you so you can use them as required.

Ideally the business card should have a Name, title, Mobile, Email , Website, Address and perhaps some social media links.

Target Market(s)

New Startups, SME's, Contract and Outsource Clients

Contact Information for Business Card

Company Name:
==============
BrambleForge Labs (UK) Ltd.

Tag Line:
========
“Digital Transformation Specialists”

Adress:
=======

Suite KR73054
14-16 Ashgrove Lane
London
E9 4PD.

Name:
=====
Idris Malek

Title: (Optional)
=============
FQTA, PgD (RNOM)

Role:
=====
Digital Solutions Architect

Email:
=====
idris@brambleforgelabs.uk

WebSite:
=======
http://www.brambleforgelabs.uk

OR

www.brambleforgelabs.uk

Mobile:
======
0044 (0)75 218 30479

OR

+44 (0)75 218 30479

LinkedIN: (Optional)
========
https://uk.linkedin.com/in/idrismalek

Skype: (Optional)
======
idris.malek

Twitter (Optional) : idrismalek

Font styles to use
Serif
Sans Serif

Requirements
Must have
• The Logo
• Business Name
• Person Name
• Title
• Mobile
• Email
• Website
• Address
• I have provided the colour scheme on my files.
Nice to have
• Twiter
• Linked in
• Facebook

```html
<!DOCTYPE html>
<html lang="en">
<head>
<meta charset="utf-8">
<title>BrambleForge Labs – Business Card</title>
<link rel="stylesheet" href="https://fonts.googleapis.com/css2?family=Raleway:wght@500;600;700;800&display=swap">
<style>
  :root {
    --brand-blue: #1563ab;
    --ink-blue: #1a5ea8;
    --teal: #1fb3c9;
    --sky: #5cc3e6;
    --orange: #f9a829;
    --paper: #ffffff;
    --edge: #b9b9b9;
    --canvas: #ffffff;
  }
  * { margin: 0; padding: 0; box-sizing: border-box; }
  html, body { width: 1200px; height: 1000px; overflow: hidden; background: var(--canvas); }
  body { position: relative; font-family: "Raleway", sans-serif; }

  .card { position: absolute; left: 247px; width: 709px; border-radius: 22px; overflow: hidden; }

  .card-front { top: 51px; height: 428px; background: var(--paper); border: 1px solid var(--edge); }
  .card-back { top: 524px; height: 427px; background: var(--brand-blue); }

  .accent-dot { position: absolute; left: -30px; top: 177px; width: 60px; height: 60px; border-radius: 50%; background: var(--orange); }

  .person { position: absolute; left: 76px; top: 186px; }
  .person-name { font-size: 31px; font-weight: 600; color: var(--ink-blue); line-height: 1.1; }
  .person-credentials { font-size: 14px; font-weight: 500; color: var(--ink-blue); margin-top: 4px; }
  .person-role { font-size: 21px; font-weight: 500; color: var(--teal); line-height: 1.03; margin-top: 6px; }

  .brand { position: absolute; right: 30px; top: 104px; text-align: right; }
  .brand-name { font-size: 44px; font-weight: 800; color: var(--ink-blue); line-height: 1; letter-spacing: -0.5px; }
  .brand-tagline { font-size: 19.5px; font-weight: 700; color: var(--teal); margin-top: 28px; letter-spacing: 0.1px; }

  .contact { position: absolute; right: 29px; top: 256px; list-style: none; }
  .contact-item { display: flex; justify-content: flex-end; align-items: center; gap: 14px; height: 35px; font-size: 16.5px; font-weight: 600; color: var(--ink-blue); }
  .contact-icon { width: 18px; height: 18px; flex: none; }

  .base-band { position: absolute; left: 0; bottom: 0; width: 709px; height: 54px; }

  .back-brand { position: absolute; left: 0; right: 0; top: 168px; text-align: center; font-size: 46px; font-weight: 800; color: var(--sky); letter-spacing: -0.5px; }
  .back-web { position: absolute; left: 173px; top: 280px; font-size: 17px; font-weight: 700; color: var(--orange); }
</style>
</head>
<body>

<section class="card card-front">
  <div class="accent-dot"></div>

  <div class="person">
    <h1 class="person-name">Idris Malek</h1>
    <p class="person-credentials">FQTA, PgD(RNOM)</p>
    <p class="person-role">Digital Solutions<br>Architect</p>
  </div>

  <div class="brand">
    <div class="brand-name">BrambleForge Labs</div>
    <p class="brand-tagline">Digital Transformation Specialists</p>
  </div>

  <ul class="contact">
    <li class="contact-item">+44 (0)75 218 30479
      <svg class="contact-icon" viewBox="0 0 18 18" aria-hidden="true"><rect x="5" y="1.5" width="8" height="15" rx="1.6" fill="none" stroke="#1fb3c9" stroke-width="1.6"/><line x1="7.5" y1="13.5" x2="10.5" y2="13.5" stroke="#1fb3c9" stroke-width="1.4"/></svg>
    </li>
    <li class="contact-item">idris.malek@brambleforgelabs.co.uk
      <svg class="contact-icon" viewBox="0 0 18 18" aria-hidden="true"><rect x="1.5" y="4" width="15" height="10" fill="#1fb3c9"/><path d="M1.5 4 L9 10 L16.5 4" fill="none" stroke="#fff" stroke-width="1.2"/></svg>
    </li>
    <li class="contact-item">14-16, Ashgrove Ln., London E9 4PD&nbsp; UK
      <svg class="contact-icon" viewBox="0 0 18 18" aria-hidden="true"><path d="M9 1 C5.4 1 3 3.6 3 6.8 C3 11 9 17.5 9 17.5 C9 17.5 15 11 15 6.8 C15 3.6 12.6 1 9 1 Z" fill="#1fb3c9"/><circle cx="9" cy="6.8" r="2.3" fill="#fff"/></svg>
    </li>
  </ul>

  <svg class="base-band" viewBox="0 0 709 54" aria-hidden="true">
    <path d="M0 32 C180 12 460 4 709 0 L709 54 L0 54 Z" fill="#f9a829"/>
  </svg>
</section>

<section class="card card-back">
  <div class="back-brand">BrambleForge Labs</div>
  <p class="back-web">www.brambleforgelabs.co.uk</p>
</section>

</body>
</html>
```